Flyer DL double sided Design Project

Hi,

Our company Harbin Panels makes kitchen and wardrobe doors. I would like an attractive and sales focused artwork for a DL flyer for general promotional use to be printed and also emailed to customers. The flyer will be a double sided, full colour and gloss finish.

We would hand out this flyer to people wanting to replace their old kitchen doors with new ones. The flyer is aimed at the general public and the Do It Yourself market as we supply the doors only, we don't measure or install.

Text will be provided but here are some guidelines:

Headline: IS YOUR KITCHEN IN NEED OF A MAKEOVER? JUST REPLACE THE DOORS SAVING YOU THOUSANDS OF $$$

This month’s special offers: Online orders only. ORDER NOW! (icon)

5 reasons to replace kitchen doors compared to a full kitchen renovation:
1. Its cheaper text, text, text
2. It's quicker text, text, text
3. It's easier text, text, text
4. It's less hassle and mess text, text, text
5. It's less wastage text, text, text

I can also provide a few high quality images of kitchens.

Reason: I won't be available to provide feedback on the design and finalise it within the deadline date. Regards, Marcia

Reason: I don't have the wording and final image today. I will be able to finalise early next week.

DO IT YOURSELF - DIY
This is mainly aimed at people who want to replace their kitchen doors themselves. People interested in improving the value of their home and saving a lot of money on their kitchen renovation.
Home owners - usually adults in the 30-50 year age bracket.

• List our website www.harbinpanels.com.au
List our email address: sales@harbinpanels.com.au
We do not measure or install. We can give quotes to customers who email a list of door sizes to us. For example: Headline: Get a quote now! Smaller print: Download a quote form (from our website www.harbinpanels.com.au) and send your door sizes for a quote today!
• Promotion: Order now and receive free delivery (on orders over $1000). Sydney metro area. Limited time only.
I like the design done by Quillmark42 with "We do wardrobe doors too" on the back of the flyer.
Delivery to your door anywhere in Australia.

```html
<!DOCTYPE html>
<html lang="en">
<head>
<meta charset="utf-8">
<title>Harbin Panels – DL Flyer</title>
<link href="https://fonts.googleapis.com/css2?family=Lobster+Two:ital,wght@0,700;1,400;1,700&family=Barlow:wght@400;600;700&family=Vollkorn+SC:wght@600&family=Vollkorn:wght@700&display=swap" rel="stylesheet">
<style>
  :root {
    --yellow: #fdd756;
    --red: #dc1e48;
    --red-dark: #b8123a;
    --rose: #c48a74;
    --ink: #262626;
    --grey: #6b6b6b;
    --white: #ffffff;
    --gold: #d9b24a;
  }
  * { box-sizing: border-box; margin: 0; padding: 0; }
  html, body { width: 1200px; height: 1191px; overflow: hidden; background: var(--white); }
  body { position: relative; font-family: "Barlow", sans-serif; color: var(--ink); }

  .panel { position: absolute; top: 63px; width: 497px; height: 1064px; overflow: hidden; background: var(--white); }
  .panel--front { left: 63px; }
  .panel--back { left: 637px; }
  .abs { position: absolute; }

  /* ---------- Front ---------- */
  .hero { left: 0; top: 0; width: 497px; height: 481px; background: var(--yellow); }
  .hero__figure { left: 0; top: 0; width: 271px; height: 481px;
    background: linear-gradient(170deg, #f6c85a 0%, #e7a0a8 55%, #d9476a 100%); opacity: .85; }
  .headline { font-family: "Lobster Two", cursive; color: var(--red); line-height: 1; white-space: nowrap; }
  .headline--small { font-style: italic; font-weight: 400; font-size: 38px; }
  .headline--big { font-style: italic; font-weight: 700;
    text-shadow: 3px 3px 0 var(--white), -2px -2px 0 var(--white), 2px -2px 0 var(--white), -2px 2px 0 var(--white), 5px 6px 0 rgba(0,0,0,.12); }
  .hl-is { right: 40px; top: 180px; }
  .hl-kitchen { right: 38px; top: 210px; font-size: 100px; }
  .hl-need { right: 43px; top: 322px; }
  .hl-makeover { right: 12px; top: 356px; font-size: 92px; }

  .tagline { left: 0; width: 497px; text-align: center; }
  .tagline__main { top: 505px; font-family: "Lobster Two", cursive; font-style: italic; font-weight: 700; font-size: 34px; color: var(--red); letter-spacing: .5px; }
  .tagline__sub { top: 556px; font-family: "Vollkorn SC", serif; font-weight: 600; font-size: 22px; color: var(--rose); letter-spacing: 1.5px; }

  .kitchen-photo { left: 0; top: 601px; width: 497px; height: 409px;
    background: linear-gradient(180deg, #3b3226 0%, #8d7d62 40%, #d8cdb4 65%, #7a5a35 100%); }

  .brand { display: flex; align-items: center; gap: 8px; }
  .brand__mark { width: 26px; height: 26px; background: var(--gold); }
  .brand__name { font-family: "Barlow", sans-serif; font-weight: 700; font-size: 19px; white-space: nowrap; }
  .brand--photo { left: 170px; top: 940px; }
  .brand--photo .brand__name { color: var(--white); }

  .footer-band { left: 0; top: 1010px; width: 497px; height: 54px; background: var(--red);
    display: flex; align-items: center; justify-content: center;
    font-family: "Barlow", sans-serif; font-weight: 700; font-size: 22px; color: var(--yellow); letter-spacing: .3px; }

  /* ---------- Back ---------- */
  .offers { left: 0; top: 0; width: 497px; height: 677px; background: var(--yellow); }
  .starburst { left: 0; top: -28px; width: 296px; height: 296px; }
  .starburst__text { left: 20px; top: 58px; width: 260px; text-align: center; transform: rotate(-13deg); color: var(--white); }
  .starburst__kicker { font-family: "Lobster Two", cursive; font-style: italic; font-weight: 700; font-size: 30px; line-height: 1; }
  .starburst__title { font-family: "Vollkorn", serif; font-weight: 700; font-size: 40px; line-height: 1; text-transform: uppercase; letter-spacing: 1px; margin-top: 4px; }

  .door-grid { left: 36px; top: 237px; display: grid; grid-template-columns: repeat(3, 83px); grid-template-rows: repeat(2, 147px); gap: 3px; }
  .door { border-radius: 2px; box-shadow: inset 0 0 0 1px rgba(0,0,0,.08); }
  .door--violet { background: linear-gradient(160deg, #9a7cc0, #7a5aa3); }
  .door--cream { background: linear-gradient(160deg, #f3f4e2, #e2e5c8); }
  .door--blue { background: linear-gradient(160deg, #74a8e2, #4d86c8); }
  .door--mint { background: linear-gradient(160deg, #bfe0df, #9cc8c8); }
  .door--ivory { background: linear-gradient(160deg, #f6f7ec, #e6e9d6); }
  .door--red { background: linear-gradient(160deg, #e0202c, #b80c18); }

  .offer-card { left: 303px; width: 156px; height: 129px; background: var(--white); border-radius: 8px;
    box-shadow: 0 2px 4px rgba(0,0,0,.12); padding: 14px 12px; }
  .offer-card--1 { top: 121px; }
  .offer-card--2 { top: 265px; }
  .offer-card--3 { top: 409px; }
  .offer-card__title { font-family: "Lobster Two", cursive; font-style: italic; font-weight: 700; font-size: 24px; color: var(--red); line-height: 1; }
  .offer-card__body { margin-top: 16px; font-size: 13.5px; line-height: 1.35; color: var(--grey); letter-spacing: .3px; }
  .offer-card__star { position: absolute; right: 10px; top: 10px; width: 20px; height: 20px; }

  .order-btn { left: 36px; top: 561px; width: 424px; height: 72px; background: var(--red); border-radius: 6px;
    box-shadow: 0 3px 0 var(--red-dark); display: flex; align-items: center; justify-content: center; gap: 22px;
    font-family: "Barlow", sans-serif; font-weight: 700; font-size: 44px; color: var(--yellow); letter-spacing: 2px; }
  .order-btn svg { width: 32px; height: 32px; }

  .web-line { left: 52px; top: 640px; display: flex; align-items: baseline; gap: 14px; }
  .web-line__url { font-weight: 700; font-size: 21px; color: var(--red); }
  .web-line__note { font-size: 13px; color: var(--ink); }

  .reasons__badge { left: 36px; top: 690px; width: 54px; height: 54px; border-radius: 50%; background: var(--rose);
    color: var(--white); display: flex; align-items: center; justify-content: center;
    font-family: "Lobster Two", cursive; font-style: italic; font-weight: 700; font-size: 38px; }
  .reasons__heading { left: 102px; top: 694px; font-family: "Lobster Two", cursive; font-style: italic; font-weight: 400; font-size: 23px; line-height: 1; color: var(--rose); }
  .reasons__heading b { font-weight: 700; }
  .reasons__heading span { display: block; font-size: 21px; margin-top: 1px; }
  .reasons__figure { left: 36px; top: 744px; width: 60px; height: 156px;
    background: linear-gradient(180deg, #f4c65a 0%, #e8a9ad 40%, #d9476a 100%); border-radius: 30px 30px 4px 4px; }
  .reasons__list { left: 114px; top: 754px; list-style: none; }
  .reasons__item { display: flex; align-items: center; gap: 6px; height: 25.8px; font-size: 16px; white-space: nowrap; }
  .reasons__num { width: 16px; height: 16px; border-radius: 50%; background: var(--rose); color: var(--white);
    font-family: "Lobster Two", cursive; font-style: italic; font-weight: 700; font-size: 12px; display: flex; align-items: center; justify-content: center; }
  .reasons__item strong { font-family: "Lobster Two", cursive; font-style: italic; font-weight: 700; font-size: 17px; }

  .contact { left: 0; top: 900px; width: 497px; height: 110px; background: var(--yellow); }
  .brand--contact { left: 36px; top: 42px; }
  .brand--contact .brand__name { color: var(--ink); font-size: 17px; }
  .contact__row { left: 178px; display: flex; align-items: center; gap: 12px; font-weight: 700; font-size: 19px; color: var(--ink); }
  .contact__row svg { width: 28px; height: 28px; }
  .contact__row--phone { top: 22px; }
  .contact__row--mail { top: 60px; }
</style>
</head>
<body>

<section class="panel panel--front">
  <div class="abs hero"></div>
  <div class="abs hero__figure" role="img" aria-label="Retro pop-art illustration of a thoughtful woman in a pink striped dress"></div>
  <div class="abs headline headline--small hl-is">Is your</div>
  <div class="abs headline headline--big hl-kitchen">Kitchen</div>
  <div class="abs headline headline--small hl-need">in need of a</div>
  <div class="abs headline headline--big hl-makeover">Makeover?</div>

  <div class="abs tagline tagline__main">Just replace the doors!</div>
  <div class="abs tagline tagline__sub">SAVING YOU THOUSANDS OF $$$</div>

  <div class="abs kitchen-photo" role="img" aria-label="Photo of a modern white kitchen with island bench and pendant lights"></div>
  <div class="abs brand brand--photo"><span class="brand__mark"></span><span class="brand__name">Harbin Panels</span></div>

  <div class="abs footer-band">www.harbinpanels.com.au</div>
</section>

<section class="panel panel--back">
  <div class="abs offers"></div>

  <svg class="abs starburst" viewBox="0 0 300 300" aria-hidden="true">
    <polygon fill="#dc1e48" points="300,150 269.7,173.8 288.6,207.4 251.4,217.8 256.1,256.1 217.8,251.4 207.4,288.6 173.8,269.7 150,300 126.2,269.7 92.6,288.6 82.2,251.4 43.9,256.1 48.6,217.8 11.4,207.4 30.3,173.8 0,150 30.3,126.2 11.4,92.6 48.6,82.2 43.9,43.9 82.2,48.6 92.6,11.4 126.2,30.3 150,0 173.8,30.3 207.4,11.4 217.8,48.6 256.1,43.9 251.4,82.2 288.6,92.6 269.7,126.2"/>
  </svg>
  <div class="abs starburst__text">
    <div class="starburst__kicker">This month’s</div>
    <div class="starburst__title">Special<br>Offers</div>
  </div>

  <div class="abs door-grid">
    <div class="door door--violet" role="img" aria-label="Violet cathedral-arch kitchen door"></div>
    <div class="door door--cream" role="img" aria-label="Cream shaker kitchen door"></div>
    <div class="door door--blue" role="img" aria-label="Blue arched glass-frame kitchen door"></div>
    <div class="door door--mint" role="img" aria-label="Mint cathedral-arch kitchen door"></div>
    <div class="door door--ivory" role="img" aria-label="Ivory shaker kitchen door"></div>
    <div class="door door--red" role="img" aria-label="Red gloss flat kitchen door"></div>
  </div>

  <div class="abs offer-card offer-card--1">
    <svg class="offer-card__star" viewBox="0 0 300 300" aria-hidden="true"><polygon fill="#c48a74" points="300,150 240,187 256,256 187,240 150,300 113,240 44,256 60,187 0,150 60,113 44,44 113,60 150,0 187,60 256,44 240,113"/></svg>
    <div class="offer-card__title">Offer 1</div>
    <div class="offer-card__body">BUY ONE GET<br>ONE FREE....etc...<br>as an example</div>
  </div>
  <div class="abs offer-card offer-card--2">
    <svg class="offer-card__star" viewBox="0 0 300 300" aria-hidden="true"><polygon fill="#c48a74" points="300,150 240,187 256,256 187,240 150,300 113,240 44,256 60,187 0,150 60,113 44,44 113,60 150,0 187,60 256,44 240,113"/></svg>
    <div class="offer-card__title">Offer 2</div>
    <div class="offer-card__body">BUY ONE GET<br>ONE FREE....etc...<br>as an example</div>
  </div>
  <div class="abs offer-card offer-card--3">
    <svg class="offer-card__star" viewBox="0 0 300 300" aria-hidden="true"><polygon fill="#c48a74" points="300,150 240,187 256,256 187,240 150,300 113,240 44,256 60,187 0,150 60,113 44,44 113,60 150,0 187,60 256,44 240,113"/></svg>
    <div class="offer-card__title">Offer 3</div>
    <div class="offer-card__body">BUY ONE GET<br>ONE FREE....etc...<br>as an example</div>
  </div>

  <div class="abs order-btn">
    <span>ORDER NOW!</span>
    <svg viewBox="0 0 32 32" aria-hidden="true"><path d="M4 3 L26 14 L16 16.5 L24 27 L20.5 29.5 L12.5 19 L6 26 Z" fill="#fdd756"/></svg>
  </div>

  <div class="abs web-line">
    <span class="web-line__url">www.harbinpanels.com.au</span>
    <span class="web-line__note">Online orders only.</span>
  </div>

  <div class="abs reasons__badge">5</div>
  <div class="abs reasons__heading"><b>reasons</b> to replace kitchen doors<span>compared to a full kitchen renovation:</span></div>
  <div class="abs reasons__figure" role="img" aria-label="Small retro illustration of a thoughtful woman"></div>
  <ol class="abs reasons__list">
    <li class="reasons__item"><span class="reasons__num">1</span><strong>It’s cheaper</strong> text, text, text......................</li>
    <li class="reasons__item"><span class="reasons__num">2</span><strong>It’s quicker</strong> text, text, text......................</li>
    <li class="reasons__item"><span class="reasons__num">3</span><strong>It’s easier</strong> text, text, text .......................</li>
    <li class="reasons__item"><span class="reasons__num">4</span><strong>It’s less hassle and mess</strong> text, text,........</li>
    <li class="reasons__item"><span class="reasons__num">5</span><strong>It’s less wastage</strong> text, text,....................</li>
  </ol>

  <div class="abs contact">
    <div class="abs brand brand--contact"><span class="brand__mark"></span><span class="brand__name">Harbin Panels</span></div>
    <div class="abs contact__row contact__row--phone">
      <svg viewBox="0 0 28 28" aria-hidden="true"><circle cx="14" cy="14" r="12.5" fill="none" stroke="#262626" stroke-width="2"/><path d="M10 7 L12.5 7 L13.5 11 L11.8 12.3 C12.6 14.2 13.8 15.4 15.7 16.2 L17 14.5 L21 15.5 L21 18 C21 19.2 20 20 18.8 20 C13 19.5 8.5 15 8 9.2 C8 8 8.8 7 10 7 Z" fill="#262626"/></svg>
      <span>(02) 5550 1834</span>
    </div>
    <div class="abs contact__row contact__row--mail">
      <svg viewBox="0 0 28 28" aria-hidden="true"><rect x="3" y="7" width="22" height="15" rx="1.5" fill="#262626"/><path d="M4 8.5 L14 16 L24 8.5" fill="none" stroke="#fdd756" stroke-width="1.8"/></svg>
      <span>sales@harbinpanels.com.au</span>
    </div>
  </div>

  <div class="abs footer-band">www.harbinpanels.com.au</div>
</section>

</body>
</html>
```